Pebble-Vane Brochure

Hello,

I want a "printed" version of the www.Pebble-Vane.net web site, so I can send it to prospect customers by physical mail.

Full Color, Letter Size paper and maximum of 8 pages.

If you need any additional information please let me know.

```html
<!DOCTYPE html>
<html lang="en">
<head>
<meta charset="utf-8">
<title>Pebble-Vane Brochure</title>
<link rel="stylesheet" href="https://fonts.googleapis.com/css2?family=Roboto+Condensed:wght@400;700&family=Lato:wght@400;700&display=swap">
<style>
:root{
  --stage:#a9a9a9;
  --navy:#141650;
  --navy-glow:#2a3a8a;
  --brand-blue:#1a7fc1;
  --brand-dark:#1b3a66;
  --sky:#29a9e8;
  --nav:#1b4b8c;
  --panel:rgba(30,34,40,.78);
  --panel-line:#b9c0c8;
  --tick:#3ec34a;
  --tile-bg:#e9eaec;
  --text-dark:#2a2f3a;
}
*{box-sizing:border-box;margin:0;padding:0}
html,body{width:1200px;height:1200px;overflow:hidden}
body{background:var(--stage);font-family:"Lato",sans-serif}
.sheet-wrap{position:absolute;left:172px;top:0;width:856px;height:1200px}
.sheet{position:absolute;left:0;top:0;width:868px;height:1216px;transform:scale(.9868);transform-origin:0 0;background:#fff;overflow:hidden}
.hero{position:absolute;left:0;top:0;width:868px;height:534px;background:linear-gradient(100deg,#e6ebf1 0%,#c4cfdb 35%,#8ea3b8 62%,#5a6f86 85%,#3d4e63 100%)}
.brand{position:absolute;left:34px;top:92px;display:flex;align-items:center;gap:8px}
.brand-dot{width:22px;height:22px;border-radius:50%;background:var(--brand-blue)}
.brand-name{font-family:"Lato",sans-serif;font-weight:700;font-size:22px;color:var(--brand-dark)}
.agent-photo{position:absolute;left:578px;top:22px;width:76px;height:80px;border-radius:50%;background:linear-gradient(160deg,#e8d7c8,#a7b6c4)}
.questions{position:absolute;left:652px;top:37px;width:190px;height:64px;background:var(--sky);border-radius:0 6px 6px 0}
.questions-title{position:absolute;left:0;right:0;top:4px;text-align:center;font-family:"Roboto Condensed",sans-serif;font-weight:700;font-size:24px;color:#fff}
.questions-cta{position:absolute;left:14px;top:36px;width:156px;height:26px;background:#fff;border-radius:13px;border:2px solid var(--sky);text-align:center;font-weight:700;font-size:13px;line-height:22px;color:var(--navy)}
.nav{position:absolute;right:28px;top:119px;font-family:"Roboto Condensed",sans-serif;font-size:12px;color:var(--nav);white-space:nowrap}
.nav span{margin:0 3px}
.headline{position:absolute;left:0;right:0;top:264px;text-align:center;font-family:"Roboto Condensed",sans-serif;font-size:28px;line-height:36px;color:#fff;text-shadow:-1px -1px 0 #111,1px -1px 0 #111,-1px 1px 0 #111,1px 1px 0 #111,0 2px 4px rgba(0,0,0,.5)}
.plan{position:absolute;top:355px;width:248px;height:148px;background:var(--panel);border:2px solid var(--panel-line);border-radius:8px;color:#fff}
.plan-title{text-align:center;font-family:"Roboto Condensed",sans-serif;font-size:15px;margin-top:12px}
.plan-specs{display:grid;grid-template-columns:1fr 1fr;gap:6px 0;padding:8px 0 0 10px;font-size:13px;list-style:none}
.plan-specs li::before{content:"• ";}
.plan-price{text-align:center;font-family:"Roboto Condensed",sans-serif;font-size:15px;margin-top:9px}
.band{position:absolute;left:0;top:534px;width:868px;height:352px;background:radial-gradient(ellipse 180px 120px at 130px 40px,var(--navy-glow),transparent),radial-gradient(ellipse 180px 120px at 406px 40px,var(--navy-glow),transparent),radial-gradient(ellipse 180px 120px at 706px 40px,var(--navy-glow),transparent),var(--navy);color:#fff}
.feature{position:absolute;top:0}
.feature-icon{position:absolute;top:-10px;width:74px;height:74px}
.feature-title{position:absolute;top:78px;width:260px;text-align:center;font-family:"Roboto Condensed",sans-serif;font-weight:700;font-size:14px;line-height:17px}
.feature-list{position:absolute;top:128px;width:250px;list-style:none;font-size:12.5px;line-height:15px}
.feature-list li{position:relative;padding-left:20px;margin-bottom:5px}
.feature-list li::before{content:"✓";position:absolute;left:0;top:0;color:var(--tick);font-weight:700}
.tiles{position:absolute;left:0;top:886px;width:868px;height:270px;background:var(--tile-bg)}
.tile{position:absolute;width:214px;height:110px;background:#fff;padding:4px;box-shadow:0 1px 3px rgba(0,0,0,.25)}
.tile-art{width:100%;height:100%;position:relative}
.tile-caption{position:absolute;left:0;right:0;bottom:0;height:24px;background:rgba(41,169,232,.85);display:flex;align-items:center;gap:8px;padding-left:8px;font-family:"Roboto Condensed",sans-serif;font-size:9px;color:#fff;text-transform:uppercase}
.tile-caption i{width:14px;height:10px;background:#fff;border-radius:5px;display:block;flex:none}
.footer{position:absolute;left:0;top:1156px;width:868px;height:60px;background:#fff;font-size:16px;color:var(--text-dark);font-weight:700}
.footer-item{position:absolute;top:20px;display:flex;align-items:center;gap:10px}
</style>
</head>
<body>
<div class="sheet-wrap">
<div class="sheet">
  <div class="hero" role="img" aria-label="Hand touching a glowing cloud with connected devices in a soft blue scene"></div>

  <div class="brand"><span class="brand-dot"></span><span class="brand-name">Pebble-Vane.net</span></div>

  <div class="agent-photo" role="img" aria-label="Support agent wearing a headset"></div>
  <div class="questions">
    <div class="questions-title">QUESTIONS?</div>
    <div class="questions-cta">CHAT WITH US</div>
  </div>

  <nav class="nav">SERVICE PRICES<span>|</span>USE CASES<span>|</span>CLOUD SERVICES<span>|</span>VANE'S INFRASTRUCTURE<span>|</span>CUSTOMER LOGIN</nav>

  <h1 class="headline">Create your own Private Cloud, Brick by Brick.<br>Virtual Data Center on dedicated Hardware</h1>

  <div class="plan" style="left:50px">
    <div class="plan-title">Starter Pebble-Vane</div>
    <ul class="plan-specs"><li>16 vCPUs</li><li>8 VLANs</li><li>32 GB RAM</li><li>10 TB Transfer</li><li>1 TB Storage</li><li>4 IP addresses</li></ul>
    <div class="plan-price">US$ 440 / month + tax</div>
  </div>
  <div class="plan" style="left:316px">
    <div class="plan-title">Professional Pebble-Vane</div>
    <ul class="plan-specs"><li>32 vCPUs</li><li>16 VLANs</li><li>64 GB RAM</li><li>20 TB Transfer</li><li>2 TB Storage</li><li>12 IP Addresses</li></ul>
    <div class="plan-price">US$ 660 / month + tax</div>
  </div>
  <div class="plan" style="left:586px">
    <div class="plan-title">Enterprise Pebble-Vane</div>
    <ul class="plan-specs"><li>64 vCPUs</li><li>32 VLANs</li><li>128 GB RAM</li><li>Unlimited</li><li>4 TB Storage</li><li>Transfer</li></ul>
    <div class="plan-price">US$ 990 / month + tax</div>
  </div>

  <section class="band">
    <div class="feature" style="left:0">
      <svg class="feature-icon" style="left:93px" viewBox="0 0 74 74"><circle cx="37" cy="37" r="35" fill="#fff"/><circle cx="37" cy="37" r="30" fill="#0b0d2a"/><path d="M24 44h26a7 7 0 0 0 0-14 10 10 0 0 0-19-3 8 8 0 0 0-7 17z" fill="none" stroke="#fff" stroke-width="3"/></svg>
      <div class="feature-title" style="left:0">BECOME A CLOUD<br>HOSTING PROVIDER</div>
      <ul class="feature-list" style="left:34px">
        <li>Start your own hosting business</li>
        <li>Sell individual virtual machines or complete virtual networks</li>
        <li>Up to three times cheaper than NimbusHost</li>
        <li>Free Virtual Data Center management software</li>
        <li>Increase your capacity when your business grows.</li>
        <li>24 x 7 x 365 Support.</li>
      </ul>
    </div>
    <div class="feature" style="left:276px">
      <svg class="feature-icon" style="left:93px" viewBox="0 0 74 74"><circle cx="37" cy="37" r="35" fill="#fff"/><circle cx="37" cy="37" r="30" fill="#0b0d2a"/><g fill="#fff"><rect x="18" y="24" width="10" height="28" rx="1"/><rect x="32" y="20" width="10" height="32" rx="1"/><rect x="46" y="24" width="10" height="28" rx="1"/></g><g stroke="#0b0d2a" stroke-width="2"><path d="M20 30h6M20 35h6M20 40h6M34 27h6M34 32h6M34 37h6M48 30h6M48 35h6M48 40h6"/></g></svg>
      <div class="feature-title" style="left:0">VIRTUALIZE YOUR SERVER<br>INFRASTRUCTURE</div>
      <ul class="feature-list" style="left:42px">
        <li>Forget about managing physical servers</li>
        <li>Rent the computer capacity you need and send your datacenter to the cloud</li>
        <li>Create virtual servers in minutes</li>
        <li>Fully redundant and dedicated physical hardware</li>
        <li>Corvex OS and Tundrix supported</li>
        <li>Connect your current network to the cloud using our Site to Site VPNs</li>
      </ul>
    </div>
    <div class="feature" style="left:576px">
      <svg class="feature-icon" style="left:93px" viewBox="0 0 74 74"><circle cx="37" cy="37" r="35" fill="#fff"/><circle cx="37" cy="37" r="30" fill="#0b0d2a"/><path d="M22 46h30a8 8 0 0 0 0-16 11 11 0 0 0-21-3 9 9 0 0 0-9 19z" fill="#fff"/><g fill="#0b0d2a"><rect x="30" y="32" width="14" height="3"/><rect x="30" y="37" width="14" height="3"/><rect x="30" y="42" width="14" height="3"/></g></svg>
      <div class="feature-title" style="left:0">MOVE FROM PUBLIC TO<br>PRIVATE CLOUD</div>
      <ul class="feature-list" style="left:28px">
        <li>Already spending more than US$ 500 per month in the public cloud?</li>
        <li>Start saving money by creating your own Private Cloud</li>
        <li>No surprises: You pay the same every month</li>
        <li>High performance Virtual Machines on dedicated hardware</li>
        <li>Easy to use web based management software</li>
      </ul>
    </div>
  </section>

  <section class="tiles">
    <div class="tile" style="left:44px;top:16px"><div class="tile-art" role="img" aria-label="Teal puzzle pieces" style="background:linear-gradient(135deg,#0d5f72,#3bbcd0)"><div class="tile-caption"><i></i>Saving money with the private cloud</div></div></div>
    <div class="tile" style="left:318px;top:16px"><div class="tile-art" role="img" aria-label="Clouds above server racks" style="background:linear-gradient(180deg,#eef3f7,#7cc6ee)"><div class="tile-caption"><i></i>Pebble-Vane technical features</div></div></div>
    <div class="tile" style="left:600px;top:16px"><div class="tile-art" role="img" aria-label="Open manual with technical sketches" style="background:linear-gradient(135deg,#f2f2f2,#9a9a9a)"><div class="tile-caption"><i></i>Pebble-Vane virtual datacenter management platform</div></div></div>
    <div class="tile" style="left:44px;top:144px"><div class="tile-art" role="img" aria-label="Business person with cloud service icons" style="background:linear-gradient(135deg,#a9d8f2,#2c4a6a)"><div class="tile-caption"><i></i>Cloud services</div></div></div>
    <div class="tile" style="left:318px;top:144px"><div class="tile-art" role="img" aria-label="Support team with headsets" style="background:linear-gradient(90deg,#d7e6f1,#c9b6a4)"><div class="tile-caption"><i></i>7x24x365 support</div></div></div>
    <div class="tile" style="left:600px;top:144px"><div class="tile-art" role="img" aria-label="Hand touching digital icons on dark blue" style="background:linear-gradient(135deg,#0c2a55,#2f7fc0)"><div class="tile-caption"><i></i>Pricing</div></div></div>
  </section>

  <footer class="footer">
    <div class="footer-item" style="left:74px">
      <svg width="16" height="14" viewBox="0 0 16 14"><rect x="1" y="3" width="14" height="10" rx="1" fill="none" stroke="#1a7fc1" stroke-width="2"/><path d="M1 4l7 5 7-5" fill="none" stroke="#1a7fc1" stroke-width="2"/></svg>
      <span>sales@pebble-vane.net</span>
    </div>
    <div class="footer-item" style="left:346px">
      <svg width="14" height="20" viewBox="0 0 14 20"><path d="M7 19S1 11 1 7a6 6 0 0 1 12 0c0 4-6 12-6 12z" fill="#1a7fc1"/><circle cx="7" cy="7" r="2.3" fill="#fff"/></svg>
      <span>450 Harbor Lane, Suite 210, Marlow Bay, FL 33000</span>
    </div>
  </footer>
</div>
</div>
</body>
</html>
```